Homepage sliders

We are a medical software company in the process of building our new site: http://www.staging.qvrdn.example/newsite/index.php
We would like three images for our homepage slider section. They would have to fit aesthetically into this section. The three sliders we had in mind:
-One slider showing multiple devices – a non-Brindle monitor, zTalker, Morvessa and eSlate
-One slider showing security (HIPAA compliancy)
-One slider showing multiple access points – at the hospital, at your practice, on the go
We do not want pictures of people. As inspiration, please use the current placeholder images on our homepage: http://www.staging.qvrdn.example/newsite/index.php
NOTE:
We are not looking for new slider designs. We only want images that would go into the current slider. Thank you!

```html
<!DOCTYPE html>
<html lang="en">
<head>
<meta charset="utf-8">
<title>Qvarden Medical</title>
<link rel="stylesheet" href="https://fonts.googleapis.com/css2?family=Lato:wght@400;700&display=swap">
<style>
  :root {
    --nav-bg: #262b33;
    --nav-text: #ffffff;
    --brand-blue: #2a95d8;
    --brand-blue-dark: #1b78b8;
    --hero-top: #ffffff;
    --hero-bottom: #f3f3f3;
    --heading: #333333;
    --body: #3a3a3a;
    --green-top: #7bab4b;
    --green-bottom: #5c8832;
    --band-bg: #ececec;
    --band-line: #d6d6d6;
    --link-blue: #1a8fd0;
    --arrow-bg: #1c1c1c;
  }
  * { box-sizing: border-box; margin: 0; padding: 0; }
  html, body { width: 1200px; height: 579px; overflow: hidden; }
  body { font-family: "Lato", sans-serif; background: var(--hero-bottom); position: relative; }

  .site-nav {
    position: absolute; left: 0; top: 0; width: 1200px; height: 55px;
    background: var(--nav-bg);
  }
  .brand {
    position: absolute; left: 76px; top: 10px;
    display: flex; align-items: center; gap: 9px;
    color: var(--nav-text); font-size: 28px; font-weight: 400; line-height: 34px;
  }
  .brand-mark { width: 24px; height: 24px; background: var(--brand-blue); }
  .nav-item {
    position: absolute; top: 18px; color: var(--nav-text);
    font-size: 14px; font-weight: 700; text-decoration: none; line-height: 18px;
  }
  .nav-caret {
    display: inline-block; margin-left: 4px; vertical-align: middle;
    border-left: 4px solid transparent; border-right: 4px solid transparent; border-top: 4px solid var(--nav-text);
  }
  .nav-cta {
    position: absolute; left: 1028px; top: 12px; width: 97px; height: 27px;
    background: linear-gradient(var(--brand-blue), var(--brand-blue-dark));
    border-radius: 4px; color: var(--nav-text); font-size: 14px; font-weight: 700;
    text-align: center; line-height: 27px; text-decoration: none;
  }

  .hero {
    position: absolute; left: 0; top: 55px; width: 1200px; height: 412px;
    background: linear-gradient(var(--hero-top), var(--hero-bottom));
    border-bottom: 1px solid var(--band-line);
  }
  .slide-image {
    position: absolute; left: 116px; top: 31px; width: 595px; height: 367px;
    background: linear-gradient(135deg, #eeeeea 0%, #dfe7e6 45%, #bfe0dd 70%, #f4f4f4 100%);
  }
  .slide-arrow {
    position: absolute; top: 176px; width: 27px; height: 27px; border-radius: 50%;
    background: var(--arrow-bg);
  }
  .slide-arrow.prev { left: 81px; }
  .slide-arrow.next { left: 1096px; }
  .slide-arrow svg { position: absolute; left: 0; top: 0; }

  .slide-copy { position: absolute; left: 723px; top: 73px; width: 320px; }
  .slide-title { font-size: 28px; font-weight: 700; color: var(--heading); line-height: 37px; }
  .slide-text { margin-top: 10px; font-size: 14px; line-height: 21.5px; color: var(--body); }
  .slide-cta {
    display: block; margin-top: 26px; width: 162px; height: 39px;
    background: linear-gradient(var(--green-top), var(--green-bottom));
    border: 1px solid #55802e; border-radius: 3px;
    color: #ffffff; font-size: 16px; font-weight: 700; text-align: center; line-height: 37px;
    text-decoration: none;
  }

  .intro-band {
    position: absolute; left: 0; top: 467px; width: 1200px; height: 112px;
    background: var(--band-bg);
  }
  .intro-text {
    position: absolute; left: 0; top: 20px; width: 1200px; text-align: center;
    font-size: 15.5px; line-height: 27px; color: var(--body);
  }
  .product-link {
    position: absolute; top: 90px; transform: translateX(-50%);
    font-size: 16px; font-weight: 700; color: var(--link-blue); text-decoration: none; white-space: nowrap;
  }
</style>
</head>
<body>
  <header class="site-nav">
    <div class="brand"><span class="brand-mark"></span>Qvarden Medical</div>
    <a class="nav-item" style="left:757px" href="#">Products<span class="nav-caret"></span></a>
    <a class="nav-item" style="left:849px" href="#">FAQ</a>
    <a class="nav-item" style="left:903px" href="#">Security</a>
    <a class="nav-item" style="left:980px" href="#">Blog</a>
    <a class="nav-cta" href="#">Get Started</a>
  </header>

  <section class="hero">
    <div class="slide-image" role="img" aria-label="Medical software dashboard shown on a desktop monitor, laptop, tablet and phone"></div>
    <span class="slide-arrow prev">
      <svg width="27" height="27" viewBox="0 0 27 27"><path d="M15.5 8.5 L10.5 13.5 L15.5 18.5" fill="none" stroke="#fff" stroke-width="2.4"/></svg>
    </span>
    <span class="slide-arrow next">
      <svg width="27" height="27" viewBox="0 0 27 27"><path d="M11.5 8.5 L16.5 13.5 L11.5 18.5" fill="none" stroke="#fff" stroke-width="2.4"/></svg>
    </span>
    <div class="slide-copy">
      <h1 class="slide-title">Say Goodbye to Lost Charges!</h1>
      <p class="slide-text">There are many variations of passages of Lorem Ipsum available, but the majority have suffered alteration in some form, by injected humour, or randomised words which don't look.</p>
      <a class="slide-cta" href="#">Get Started Now!</a>
    </div>
  </section>

  <section class="intro-band">
    <p class="intro-text">Cras aliquam, quam ut ornare mollis, eros sapien faucibus ligula, quis ullamcorper erat dui eget turpis. Nullam interdum commodo augue eu dignissim.<br>Maecenas pellentesque erat quis ipsum suscipit ullamcorper. Nulla vehicula laoreet orci ut luctus. Pellentesque at nibh purus.</p>
    <a class="product-link" style="left:199px" href="#">SignOut</a>
    <a class="product-link" style="left:440px" href="#">Charge Capture</a>
    <a class="product-link" style="left:682px" href="#">SBAR</a>
    <a class="product-link" style="left:923px" href="#">Anesthesiology</a>
  </section>
</body>
</html>
```